Visitenkarten-Design für architect i.a.
Aufgabenstellung
Logo ( Siehe Anhang)
scrinari
dessignader da construcziun aulta
maturitad professiunla
architect i.a.

```html
<!DOCTYPE html>
<html lang="rm">
<head>
<meta charset="utf-8">
<title>Visitenkarte – torvel</title>
<link href="https://fonts.googleapis.com/css2?family=Questrial&display=swap" rel="stylesheet">
<style>
  :root {
    --sky: #94d3ef;
    --slate: #537786;
    --ink: #4f4f52;
    --mark: #58595b;
    --paper: #ffffff;
    --backdrop: #eef0f1;
  }
  html, body {
    margin: 0;
    padding: 0;
    width: 1200px;
    height: 1200px;
    overflow: hidden;
    background: var(--backdrop);
    font-family: "Questrial", "Century Gothic", sans-serif;
    color: var(--ink);
  }
  .canvas {
    position: relative;
    width: 1200px;
    height: 1200px;
  }
  .card {
    position: absolute;
    top: 290px;
    width: 406px;
    height: 620px;
    background: var(--paper);
    box-shadow: 0 6px 24px rgba(0,0,0,0.12);
    overflow: hidden;
  }
  .card--back { left: 156px; }
  .card--front { left: 622px; }
  .card__corners {
    position: absolute;
    inset: 0;
    width: 100%;
    height: 100%;
  }
  .corner--sky { fill: var(--sky); }
  .corner--slate { fill: var(--slate); }

  .contact {
    position: absolute;
    left: 0;
    right: 0;
    text-align: center;
    font-size: 22px;
    line-height: 31px;
    font-style: normal;
  }
  .contact__address { top: 193px; }
  .contact__lines { top: 340px; }
  .contact__row {
    display: flex;
    align-items: center;
    justify-content: center;
    gap: 6px;
    height: 40px;
  }
  .contact__icon { width: 20px; height: 20px; }
  .contact__icon circle { fill: var(--slate); }
  .icon-glyph--fill { fill: #fff; }
  .icon-glyph--line { fill: none; stroke: #fff; stroke-width: 1.4; stroke-linejoin: round; stroke-linecap: round; }

  .brand {
    position: absolute;
    left: 0;
    right: 0;
    top: 178px;
    text-align: center;
  }
  .brand__name {
    display: inline-flex;
    align-items: center;
    gap: 14px;
    font-size: 68px;
    line-height: 1;
    color: var(--mark);
    letter-spacing: 1px;
  }
  .brand__square {
    width: 22px;
    height: 22px;
    background: var(--sky);
  }
  .titles {
    position: absolute;
    left: 0;
    right: 0;
    top: 320px;
    text-align: center;
    font-size: 23px;
    line-height: 31px;
    margin: 0;
  }
</style>
</head>
<body>
<main class="canvas">

  <section class="card card--back" aria-label="Kontaktseite">
    <svg class="card__corners" viewBox="0 0 270 413" preserveAspectRatio="none" aria-hidden="true">
      <polygon class="corner--sky" points="0,0 145,0 0,97"/>
      <polygon class="corner--slate" points="0,321 171,413 0,413"/>
    </svg>
    <address class="contact contact__address">
      Torvel Kinst<br>
      Lindenmattweg 17<br>
      6015 Luzern
    </address>
    <div class="contact contact__lines">
      <div class="contact__row">
        <svg class="contact__icon" viewBox="0 0 20 20" aria-hidden="true">
          <circle cx="10" cy="10" r="10"/>
          <path class="icon-glyph--fill" d="M6.5 5.5 L8.3 5.2 L9.2 7.6 L8 8.6 Q9 10.9 11.4 12 L12.4 10.8 L14.8 11.7 L14.5 13.5 Q9.5 14.5 6.5 9.5 Q6 7 6.5 5.5 Z"/>
        </svg>
        <span>079 412 57 90</span>
      </div>
      <div class="contact__row">
        <svg class="contact__icon" viewBox="0 0 20 20" aria-hidden="true">
          <circle cx="10" cy="10" r="10"/>
          <path class="icon-glyph--line" d="M5 6.5 H15 V13.5 H5 Z M5 6.5 L10 10.5 L15 6.5"/>
        </svg>
        <span>torvelkinst@alpenpost.ch</span>
      </div>
    </div>
  </section>

  <section class="card card--front" aria-label="Vorderseite">
    <svg class="card__corners" viewBox="0 0 271 413" preserveAspectRatio="none" aria-hidden="true">
      <polygon class="corner--slate" points="115,0 271,0 271,65"/>
      <polygon class="corner--sky" points="271,267 271,413 112,413"/>
    </svg>
    <div class="brand">
      <span class="brand__name"><span class="brand__square"></span>torvel</span>
    </div>
    <p class="titles">
      Designer des Baues aulta<br>
      Maturitad professiunla<br>
      Architekt i.a.
    </p>
  </section>

</main>
</body>
</html>
```